Business Card Design Project

A polished, very professional looking business card. I think we want to keep it all grey. I've attached our old logo, and current mockup in which case we really like the font.

Target Market(s)

Target Market are Bride and Grooms and Wedding Coordinators. We are wedding photographers

Industry/Entity Type

Business

Font styles to use
Serif
Sans Serif

Requirements
Must have
• An elegant, yet simple and sophisticated appearance.

Phone number, Email, Website and Social Media link.
Nice to have
• An element that can be spot glossed when printed. Not necessary though.
Should not have
• Bright colors, images or intensive graphics.

```html
<!DOCTYPE html>
<html lang="en">
<head>
<meta charset="utf-8">
<title>Grant Whitlow Photographers – Business Card Concepts</title>
<link rel="stylesheet" href="https://fonts.googleapis.com/css2?family=Cormorant+SC:wght@500&family=Source+Sans+3:wght@400&display=swap">
<style>
  :root {
    --canvas: #ffffff;
    --card-border: #c8c8c8;
    --mark-grey: #58595b;
    --soft-grey: #a7a9ac;
    --pale-grey: #d6d7d8;
    --ink-dark: #4d4d4f;
    --ink-light: #ffffff;
    --night: #151515;
    --charcoal: #2b2b2b;
    --silver: #c4c5c6;
    --bronze: #6f5336;
    --gold: #c9a44c;
    --gold-deep: #7a6226;
  }
  * { box-sizing: border-box; margin: 0; padding: 0; }
  html, body { width: 1200px; height: 482px; overflow: hidden; background: var(--canvas); }
  .sheet { position: relative; width: 1200px; height: 482px; }

  .card { position: absolute; width: 382px; height: 229px; overflow: hidden; }
  .card--front { top: 0; }
  .card--back { top: 253px; }
  .col-1 { left: 0; }
  .col-2 { left: 412px; }
  .col-3 { left: 818px; }

  .card__art { position: absolute; inset: 0; width: 100%; height: 100%; }

  .card--white { background: var(--canvas); border: 1px solid var(--card-border); }
  .card--silver-bg { background: var(--night); }
  .card--gold-bg { background: var(--night); }

  .brand { position: absolute; text-align: center; }
  .brand__mark { display: block; width: 27px; height: 27px; margin: 0 auto 17px; }
  .brand__name {
    font-family: "Cormorant SC", "Times New Roman", serif;
    font-weight: 500; font-size: 20px; letter-spacing: 3.6px; line-height: 1;
    white-space: nowrap;
  }
  .brand__tag {
    font-family: "Source Sans 3", Arial, sans-serif;
    font-size: 5.5px; letter-spacing: 3.2px; margin-top: 6px;
  }

  .card--white .brand { left: 184px; top: 101px; width: 182px; color: var(--ink-dark); }
  .card--white .brand__mark { background: var(--mark-grey); }
  .card--silver-bg .brand,
  .card--gold-bg .brand { left: 24px; top: 112px; width: 178px; color: var(--ink-light); }
  .card--silver-bg .brand__mark,
  .card--gold-bg .brand__mark { background: var(--soft-grey); }
  .card--silver-bg .brand__tag,
  .card--gold-bg .brand__tag { color: var(--soft-grey); }

  .card--back-grey { background: var(--soft-grey); }
  .card--back-bronze { background: var(--bronze); }
  .contact {
    position: absolute; left: 0; right: 0; top: 156px;
    list-style: none; text-align: center; color: var(--ink-light);
    font-family: "Source Sans 3", Arial, sans-serif; font-size: 11.2px; line-height: 14.4px;
  }
  .col-2 .contact { top: 150px; }
</style>
</head>
<body>
<main class="sheet">

  <section class="card card--front card--white col-1">
    <svg class="card__art" viewBox="0 0 382 229" role="img" aria-label="Grey film strip frames sweeping across the card">
      <defs>
        <linearGradient id="film-grey" x1="0" y1="0" x2="1" y2="1">
          <stop offset="0" stop-color="#a7a9ac" stop-opacity="0.85"/>
          <stop offset="1" stop-color="#a7a9ac" stop-opacity="0.15"/>
        </linearGradient>
      </defs>
      <polygon points="0,0 382,0 382,20 230,30 175,150 0,160" fill="url(#film-grey)"/>
      <polygon points="0,160 260,229 0,229" fill="url(#film-grey)" opacity="0.6"/>
    </svg>
    <div class="brand">
      <span class="brand__mark"></span>
      <p class="brand__name">Grant Whitlow</p>
      <p class="brand__tag">PHOTOGRAPHERS</p>
    </div>
  </section>

  <section class="card card--front card--silver-bg col-2">
    <svg class="card__art" viewBox="0 0 382 229" role="img" aria-label="Scratched black and silver film strip texture">
      <defs>
        <linearGradient id="silver-tone" x1="0" y1="0.3" x2="1" y2="0.7">
          <stop offset="0" stop-color="#3a3a3a"/>
          <stop offset="0.3" stop-color="#151515"/>
          <stop offset="0.6" stop-color="#2b2b2b"/>
          <stop offset="1" stop-color="#c4c5c6"/>
        </linearGradient>
      </defs>
      <rect width="382" height="229" fill="url(#silver-tone)"/>
    </svg>
    <div class="brand">
      <span class="brand__mark"></span>
      <p class="brand__name">Grant Whitlow</p>
      <p class="brand__tag">PHOTOGRAPHERS</p>
    </div>
  </section>

  <section class="card card--front card--gold-bg col-3">
    <svg class="card__art" viewBox="0 0 382 229" role="img" aria-label="Scratched black and gold film strip texture">
      <defs>
        <linearGradient id="gold-tone" x1="0" y1="0.3" x2="1" y2="0.7">
          <stop offset="0" stop-color="#7a6226"/>
          <stop offset="0.3" stop-color="#14130f"/>
          <stop offset="0.6" stop-color="#2a2516"/>
          <stop offset="1" stop-color="#c9a44c"/>
        </linearGradient>
      </defs>
      <rect width="382" height="229" fill="url(#gold-tone)"/>
    </svg>
    <div class="brand">
      <span class="brand__mark"></span>
      <p class="brand__name">Grant Whitlow</p>
      <p class="brand__tag">PHOTOGRAPHERS</p>
    </div>
  </section>

  <section class="card card--back card--back-grey col-1">
    <ul class="contact">
      <li>Email: grant@grantwhitlow.com</li>
      <li>Phone: 555.210.4826</li>
      <li>Website: www.grantwhitlow.com</li>
      <li>Social Media: socialpage.com/GrantWhitlowPhoto</li>
    </ul>
  </section>

  <section class="card card--back card--back-grey col-2">
    <ul class="contact">
      <li>Email: grant@grantwhitlow.com</li>
      <li>Phone: 555.210.4826</li>
      <li>Website: www.grantwhitlow.com</li>
      <li>Social Media: socialpage.com/GrantWhitlowPhoto</li>
    </ul>
  </section>

  <section class="card card--back card--back-bronze col-3">
    <ul class="contact">
      <li>Email: grant@grantwhitlow.com</li>
      <li>Phone: 555.210.4826</li>
      <li>Website: www.grantwhitlow.com</li>
      <li>Social Media: socialpage.com/GrantWhitlowPhoto</li>
    </ul>
  </section>

</main>
</body>
</html>
```